Business Card Design - Cryotherapy

We need a custom created business card for our company FrostLeaf Spa. We provide whole body cryotherapy and localized cryotherapy to our clients. Please be creative.
Please see our website for idea's on design.
www.frostleafspa-example.com
Industry/Entity Type
Business
Contact Information for Business Card
Name, Position, Phone Number, Address, Website, Email
Look and feel
Each slider illustrates characteristics of the customer's brand and the style your logo design should communicate.

```html
<!DOCTYPE html>
<html lang="en">
<head>
<meta charset="utf-8">
<title>FrostLeaf Spa — Business Card</title>
<link href="https://fonts.googleapis.com/css2?family=Arimo:wght@400;500&family=Old+Standard+TT:wght@700&display=swap" rel="stylesheet">
<style>
  :root {
    --teal: #0aa0b9;
    --teal-deep: #039bb4;
    --green: #00733a;
    --green-mid: #008a5c;
    --ink: #111111;
    --paper: #ffffff;
    --backdrop: #e9e6e1;
  }
  * { margin: 0; padding: 0; box-sizing: border-box; }
  html, body {
    width: 1189px; height: 1200px; overflow: hidden;
    background: var(--backdrop);
    font-family: "Arimo", Arial, sans-serif;
  }
  .canvas { position: relative; width: 1189px; height: 1200px; }

  .card {
    position: absolute; left: 140px; width: 917px; height: 523px;
    box-shadow: 2px 4px 10px rgba(0,0,0,0.35);
  }

  /* Front */
  .card--front {
    top: 47px;
    background: linear-gradient(to bottom, var(--teal) 0%, var(--green) 100%);
    padding: 10px;
  }
  .card--front .face {
    position: relative; width: 100%; height: 100%;
    background: var(--paper); text-align: center;
  }
  .wordmark {
    position: absolute; left: 0; right: 0;
    display: flex; align-items: center; justify-content: center; gap: 18px;
    font-family: "Arimo", Arial, sans-serif; font-weight: 500;
    letter-spacing: 1px; white-space: nowrap;
  }
  .wordmark__dot { border-radius: 50%; flex: none; }
  .card--front .wordmark { top: 135px; font-size: 64px; color: var(--green); }
  .card--front .wordmark__dot { width: 46px; height: 46px; background: var(--teal); }

  .divider {
    position: absolute; left: 64px; right: 64px; top: 250px;
    height: 3px; background: var(--ink);
  }
  .person__name {
    position: absolute; left: 0; right: 0; top: 255px;
    font-family: "Old Standard TT", Georgia, serif; font-weight: 700;
    font-size: 43px; color: var(--teal-deep); line-height: 1.2;
  }
  .person__role {
    position: absolute; left: 0; right: 0; top: 306px;
    font-size: 31px; font-weight: 500; color: var(--ink);
  }
  .contact {
    position: absolute; left: 0; right: 0; top: 357px;
    list-style: none; font-size: 23px; color: var(--ink); line-height: 32.5px;
  }
  .contact__address { margin-top: 2px; }

  /* Back */
  .card--back {
    top: 623px;
    background: var(--paper);
    padding: 10px;
  }
  .card--back .face {
    position: relative; width: 100%; height: 100%;
    background: linear-gradient(to bottom, var(--teal-deep) 0%, var(--green-mid) 50%, var(--green) 100%);
  }
  .card--back .wordmark { top: 210px; font-size: 74px; color: var(--paper); }
  .card--back .wordmark__dot { width: 54px; height: 54px; background: rgba(255,255,255,0.85); }
</style>
</head>
<body>
<main class="canvas">
  <section class="card card--front" aria-label="Business card front">
    <div class="face">
      <div class="wordmark"><span class="wordmark__dot"></span><span class="wordmark__name">FROSTLEAF SPA</span></div>
      <div class="divider"></div>
      <h1 class="person__name">Marissa Holloway</h1>
      <p class="person__role">Managing Director</p>
      <ul class="contact">
        <li>(555) 014-2290</li>
        <li>info@frostleafspa-example.com</li>
        <li>www.frostleafspa-example.com</li>
        <li class="contact__address">420 Lakeview Avenue, Suite 210, Springfield, IL 60000</li>
      </ul>
    </div>
  </section>

  <section class="card card--back" aria-label="Business card back">
    <div class="face">
      <div class="wordmark"><span class="wordmark__dot"></span><span class="wordmark__name">FROSTLEAF SPA</span></div>
    </div>
  </section>
</main>
</body>
</html>
```